Pebble

My company name is pebble. The logo is attached. I am the business owner.
Name Gideon Thorpe
Phone number- 5553018826
email- Gideon_thorpe@quillnet.net
Website is not live yet but it will be workwithpebble.com
the current beta link is- https://site.brvhosting.com/pebble-v3/
on the back write “ find creative pros”
Use that beta link as reference for typography and colors on card.

```html
<!DOCTYPE html>
<html lang="en">
<head>
<meta charset="utf-8">
<title>Pebble — Business Card</title>
<link href="https://fonts.googleapis.com/css2?family=Open+Sans:wght@400;700&display=swap" rel="stylesheet">
<style>
  :root {
    --stage: #939598;
    --paper: #ffffff;
    --ink-dark: #060709;
    --accent: #c44a28;
    --logo-light: #dcdcdc;
    --text-gray: #6a6a6a;
    --white: #ffffff;
  }
  * { margin: 0; padding: 0; box-sizing: border-box; }
  html, body {
    width: 1200px; height: 960px; overflow: hidden;
    background: var(--stage);
    font-family: "Open Sans", Arial, sans-serif;
  }
  .canvas { position: relative; width: 1200px; height: 960px; }

  .card { position: absolute; width: 756.8px; height: 432px; overflow: hidden; }
  .card--front { left: 130.4px; top: 43.2px; background: var(--paper); }
  .card--back { left: 264.8px; top: 504px; background: var(--ink-dark); }

  .wordmark {
    position: absolute; font-weight: 700; line-height: 1; letter-spacing: -1px;
    white-space: nowrap;
  }
  .card--front .wordmark {
    left: 42px; top: 122px; font-size: 78px; color: var(--logo-light);
  }
  .card--back .wordmark {
    left: 0; right: 0; text-align: center; top: 162px; font-size: 94px; color: var(--white);
  }

  .name-band { position: absolute; left: 0; top: 0; width: 756.8px; height: 432px; }
  .name-band .accent { fill: var(--accent); }

  .holder-name {
    position: absolute; left: 36px; top: 229px;
    font-size: 34px; line-height: 46px; color: var(--white); font-weight: 400;
  }

  .contact-list { list-style: none; }
  .contact-item { position: absolute; left: 0; height: 22.4px; width: 600px; }
  .contact-item--phone { top: 306.4px; }
  .contact-item--mail { top: 336.8px; }
  .contact-item--web { top: 366.4px; }
  .contact-tab {
    position: absolute; left: 0; top: 0; width: 57.6px; height: 22.4px;
    background: var(--accent);
  }
  .contact-tab svg { position: absolute; left: 35px; top: 2.2px; width: 18px; height: 18px; }
  .contact-text {
    position: absolute; left: 81.6px; top: 0; line-height: 22.4px;
    font-size: 19px; color: var(--text-gray);
  }

  .tagline-band {
    position: absolute; left: 0; top: 336px; width: 100%; height: 27.2px;
    background: var(--accent);
    color: var(--white); text-align: center;
    font-size: 18px; line-height: 27.2px; letter-spacing: 8.6px; text-indent: 8px;
  }
</style>
</head>
<body>
<main class="canvas">

  <section class="card card--front" aria-label="Card front">
    <div class="wordmark">PEBBLE</div>

    <svg class="name-band" viewBox="0 0 756.8 432" aria-hidden="true">
      <polygon class="accent" points="0,224.8 308,224.8 333.6,277.6 0,277.6"/>
      <rect class="accent" x="317.6" y="244.8" width="439.2" height="22.4"/>
    </svg>
    <h1 class="holder-name">Gideon Thorpe</h1>

    <ul class="contact-list">
      <li class="contact-item contact-item--phone">
        <span class="contact-tab">
          <svg viewBox="0 0 18 18" aria-hidden="true">
            <rect x="1" y="1" width="16" height="16" rx="3" fill="#fff"/>
            <path d="M6.5 4 L8 4 L8.6 6.6 L7.6 7.4 Q8.4 9.6 10.4 10.6 L11.2 9.6 L13.6 10.4 L13.6 12 Q13 13.6 11 13.2 Q6 11.6 5 6 Q5 4.4 6.5 4 Z" fill="var(--accent)"/>
          </svg>
        </span>
        <span class="contact-text">5553018826</span>
      </li>
      <li class="contact-item contact-item--mail">
        <span class="contact-tab">
          <svg viewBox="0 0 18 18" aria-hidden="true">
            <path d="M2 7 L9 2 L16 7 L16 15 L2 15 Z" fill="#fff"/>
            <path d="M4.5 8.5 L9 11.5 L13.5 8.5" stroke="var(--accent)" stroke-width="1.6" fill="none"/>
          </svg>
        </span>
        <span class="contact-text">Gideon_thorpe@quillnet.net</span>
      </li>
      <li class="contact-item contact-item--web">
        <span class="contact-tab">
          <svg viewBox="0 0 18 18" aria-hidden="true">
            <g fill="none" stroke="#fff" stroke-width="1.3">
              <circle cx="9" cy="9" r="7.3"/>
              <ellipse cx="9" cy="9" rx="3.2" ry="7.3"/>
              <line x1="1.7" y1="9" x2="16.3" y2="9"/>
              <line x1="9" y1="1.7" x2="9" y2="16.3"/>
              <line x1="3" y1="5.5" x2="15" y2="5.5"/>
              <line x1="3" y1="12.5" x2="15" y2="12.5"/>
            </g>
          </svg>
        </span>
        <span class="contact-text">workwithpebble.com</span>
      </li>
    </ul>
  </section>

  <section class="card card--back" aria-label="Card back">
    <div class="wordmark">PEBBLE</div>
    <p class="tagline-band">FIND CREATIVE PROS</p>
  </section>

</main>
</body>
</html>
```